Coffee and fruit juice

We are a malaysian restaurant that also serves aussie coffee and breakfast from 7am to 11am. After 11am we serve malaysian food but we also have a salad and sandwhich bar for people to choose from. We need a poster to hang outside our door to let people know that we are now also serving aussie coffee and breakfast as well as our usual malaysian cuisine.

Target Market(s)

Office location

Industry/Entity Type

Restaurant

Font styles to use
Decorative
Script

Requirements
Must have
• images and word
Nice to have
• something bold to attract people's attention

```html
<!DOCTYPE html>
<html lang="en">
<head>
<meta charset="utf-8">
<title>Now Serving Poster</title>
<link rel="stylesheet" href="https://fonts.googleapis.com/css2?family=Oswald:wght@500;600&family=EB+Garamond:ital@1&display=swap">
<style>
  :root {
    --ink: #000000;
    --paper: #ffffff;
  }
  html, body {
    margin: 0;
    padding: 0;
    overflow: hidden;
    background: var(--ink);
  }
  .poster {
    position: relative;
    width: 900px;
    height: 1200px;
    background: var(--ink);
    color: var(--paper);
    overflow: hidden;
  }
  .headline {
    position: absolute;
    top: 138px;
    left: 0;
    width: 900px;
    margin: 0;
    text-align: center;
    font-family: 'Oswald', sans-serif;
    font-weight: 600;
    font-size: 88px;
    letter-spacing: 7px;
    line-height: 1;
  }
  .rule {
    position: absolute;
    height: 13px;
    background: var(--paper);
  }
  .rule--top { top: 268px; left: 149px; width: 606px; }
  .rule--bottom { top: 963px; left: 153px; width: 606px; }
  .offer {
    position: absolute;
    top: 418px;
    left: 0;
    width: 900px;
    margin: 0;
    text-align: center;
    font-family: 'EB Garamond', serif;
    font-style: italic;
    font-size: 132px;
    line-height: 134px;
  }
  .footnote {
    position: absolute;
    top: 1006px;
    left: 0;
    width: 910px;
    margin: 0;
    text-align: center;
    font-family: 'Oswald', sans-serif;
    font-weight: 500;
    font-size: 36px;
    letter-spacing: 0.5px;
    line-height: 1.2;
  }
</style>
</head>
<body>
  <main class="poster">
    <h1 class="headline">NOW SERVING</h1>
    <div class="rule rule--top"></div>
    <p class="offer">aussie<br>coffee &amp;<br>breakfast*</p>
    <div class="rule rule--bottom"></div>
    <p class="footnote">*as well as our usual malaysian cuisine</p>
  </main>
</body>
</html>
```